New Wine Label - Argentinian Malbec 'Viento Callado'

I am looking for an exceptional and exciting design for a wine label called 'Viento Callado' meaning Quiet Wind or Wind of the Quiet. The design must feature the name 'Viento Callado', a star logo and the word 'Malbec'. It will also need the words 'Mendoza, Argentina' at the bottom of the label as a prominent piece of information. Please produce the work in size 80mm x 100mm. Feel free to use colour in addition to black/white and ensue that the label is easy to read on a shelf placement.

Target Market(s)

25-50 Year Olds who enjoy great wine that looks and appears interesting and a little different.

Requirements
Must have
• Star Logo
• Word - Malbec
• Words - Mendoza, Argentina
Nice to have
• Background image to label

```html
<!DOCTYPE html>
<html lang="en">
<head>
<meta charset="utf-8">
<title>Viento Callado – Malbec Label</title>
<link rel="stylesheet" href="https://fonts.googleapis.com/css2?family=Kaushan+Script&display=swap">
<style>
  :root {
    --backdrop: #e3e8ef;
    --ink: #0d0d0d;
    --paper: #fbfaf6;
    --stone: #8c8c8c;
    --gold: #d8b65c;
    --gold-soft: #f0d9a0;
    --split: 324px;
  }
  html, body {
    margin: 0;
    padding: 0;
    width: 1138px;
    height: 1200px;
    overflow: hidden;
    background: var(--backdrop);
  }
  .label {
    position: absolute;
    left: 209px;
    top: 160px;
    width: 720px;
    height: 880px;
    overflow: hidden;
    background: var(--paper);
    box-shadow: 0 10px 30px rgba(20, 30, 50, 0.18);
    font-family: "Kaushan Script", cursive;
  }
  .quadrant { position: absolute; }
  .quadrant--upper-left { left: 0; top: 0; width: var(--split); height: 320px; background: var(--stone); }
  .quadrant--upper-left svg { display: block; }
  .quadrant--upper-right {
    left: var(--split); top: 0; right: 0; height: 320px;
    background: linear-gradient(160deg, #fffdf7 0%, #f7f1e2 100%);
  }
  .quadrant--lower-left {
    left: 0; top: 424px; width: var(--split); bottom: 0;
    background: linear-gradient(180deg, #8f8f8f 0%, #9c9c9c 100%);
  }
  .quadrant--lower-right {
    left: var(--split); top: 424px; right: 0; bottom: 0;
    background: linear-gradient(200deg, #fffdf8 0%, #f6efe4 100%);
  }
  .name-band {
    position: absolute;
    left: 0; right: 0; top: 320px; height: 104px;
    display: flex;
  }
  .name-band__light, .name-band__dark {
    display: flex;
    align-items: center;
    font-size: 92px;
    line-height: 1;
    color: var(--gold);
  }
  .name-band__light {
    width: var(--split);
    background: var(--paper);
    justify-content: flex-end;
    padding-right: 12px;
    box-sizing: border-box;
  }
  .name-band__dark {
    flex: 1;
    background: var(--ink);
    padding-left: 16px;
  }
  .varietal {
    position: absolute;
    left: calc(var(--split) - 72px);
    top: 40px;
    width: 144px;
    height: 144px;
    border-radius: 50%;
    background: radial-gradient(circle, var(--gold-soft) 0%, var(--gold) 75%, rgba(216, 182, 92, 0.6) 100%);
    display: flex;
    align-items: center;
    justify-content: center;
    font-size: 34px;
    color: var(--ink);
  }
  .origin {
    position: absolute;
    left: 0; right: 0; bottom: 46px;
    display: flex;
    font-size: 56px;
    line-height: 1;
  }
  .origin__region {
    width: var(--split);
    text-align: right;
    padding-right: 14px;
    box-sizing: border-box;
    color: #ffffff;
  }
  .origin__country { color: var(--ink); }
</style>
</head>
<body>
  <main class="label">
    <div class="quadrant quadrant--upper-left">
      <svg width="324" height="320" viewBox="0 0 324 320" role="img" aria-label="Dark arc with fine curved line texture">
        <path d="M324 0 L30 0 A294 294 0 0 0 324 294 Z" fill="#141414"/>
      </svg>
    </div>
    <div class="quadrant quadrant--upper-right" role="img" aria-label="Fine gold guilloche mesh texture"></div>
    <div class="quadrant quadrant--lower-left" role="img" aria-label="Grey panel with fine curved line texture"></div>
    <div class="quadrant quadrant--lower-right" role="img" aria-label="Fine pale gold guilloche mesh texture"></div>

    <div class="name-band">
      <span class="name-band__light">Viento</span>
      <span class="name-band__dark">Callado</span>
    </div>

    <div class="varietal">Malbec</div>

    <p class="origin" style="margin:0">
      <span class="origin__region">Mendoza,</span>
      <span class="origin__country">Argentina</span>
    </p>
  </main>
</body>
</html>
```